Silken Roam (A luxury Travel Website)

website text attached in document below

images also attached

feel free to use other images if needed

Target Market(s)

Luxury Seekers and wealthy couples / families

Industry/Entity Type

Luxury Travel

Coding

Coded - Design and coding required

Number of Pages Required

1 page

Requirements
Must have
• A luxury design and easy use.
Nice to have
• Ease of use of page, incorporation of images into the flow of the site

```html
<!DOCTYPE html>
<html lang="en">
<head>
<meta charset="utf-8">
<title>Silken Roam</title>
<link href="https://fonts.googleapis.com/css2?family=Gilda+Display&family=Poppins:wght@400;500;600;700&display=swap" rel="stylesheet">
<style>
:root{
  --bg:#000;
  --hero-top:#1c1c1c;
  --ink:#f3f1ec;
  --muted:#cfcfcf;
  --line:#6b6b6b;
  --accent:#8fc3ea;
  --accent-deep:#3d7fb8;
  --btn-ink:#0c2233;
}
*{margin:0;padding:0;box-sizing:border-box}
html,body{width:1200px;height:2783px;overflow:hidden;background:var(--bg)}
body{position:relative;font-family:"Poppins",sans-serif;color:var(--ink)}
.abs{position:absolute}
.hero-bg{left:0;top:0;width:1200px;height:520px;background:radial-gradient(ellipse at 60% 30%,#2a2a2a 0%,var(--hero-top) 45%,#050505 100%)}
.plans-bg{left:0;top:2110px;width:1200px;height:585px;background:linear-gradient(180deg,#000 0%,#17130e 35%,#1d150c 70%,#0b0805 100%)}
.footer-bg{left:0;top:2695px;width:1200px;height:88px;background:#0c0a08;border-top:1px solid #2a2520}
.brand{left:0;top:36px;width:1200px;text-align:center;font-family:"Gilda Display",serif;font-size:27px;letter-spacing:1px;color:var(--accent)}
.eyebrow{font-family:"Gilda Display",serif;font-size:17px;letter-spacing:4px;color:var(--ink)}
.eyebrow-sans{font-family:"Poppins",sans-serif;font-size:12px;letter-spacing:2.5px;color:var(--ink)}
.rule{height:1px;background:var(--line)}
.display{font-family:"Gilda Display",serif;font-weight:400;line-height:1.05}
.lede{font-size:13px;color:var(--ink)}
.btn{display:block}
.btn .frame{position:absolute;left:4px;top:4px;right:-4px;bottom:-4px;border:1px solid var(--accent-deep)}
.btn .face{position:absolute;inset:0;background:linear-gradient(180deg,#bfe0f6 0%,var(--accent) 55%,#6aa8db 100%);display:flex;align-items:center;justify-content:center;font-size:11px;font-weight:700;letter-spacing:1.2px;color:var(--btn-ink)}
.photo{position:absolute}
.field{left:269px;top:2301px;width:662px;height:156px;border:1px solid #8a8a8a;background:rgba(0,0,0,.25)}
.field span{position:absolute;left:31px;top:22px;font-size:12px;color:var(--muted)}
.copy{left:225px;top:2730px;font-size:11px;color:#9a9a9a}
.copy b{color:var(--ink);font-weight:600}
.social{width:38px;height:38px;border-radius:50%;background:#222;border:1px solid #333}
</style>
</head>
<body>
<div class="abs hero-bg" role="img" aria-label="Faint dark photo of a private jet in flight"></div>
<div class="abs plans-bg" role="img" aria-label="Dim night photo of overwater villas with reflected lights"></div>
<div class="abs footer-bg"></div>

<header class="abs brand">SILKEN ROAM</header>

<section class="hero">
  <div class="abs rule" style="left:310px;top:165px;width:139px"></div>
  <p class="abs eyebrow" style="left:449px;top:153px;width:305px;text-align:center">LOOKING TO STAY AT A</p>
  <div class="abs rule" style="left:754px;top:165px;width:139px"></div>
  <h1 class="abs display" style="left:0;top:188px;width:1200px;text-align:center;font-size:56px">5 Star Hotel or to Fly Business<br>Class Anywhere?</h1>
  <p class="abs lede" style="left:0;top:318px;width:1200px;text-align:center">Share a screenshot of your travel plans and we beat the price, within 24 hours.</p>
  <a class="abs btn" style="left:522px;top:369px;width:152px;height:39px"><span class="frame"></span><span class="face">ADD SCREENSHOT</span></a>
</section>

<section class="gallery">
  <div class="photo" style="left:66px;top:557px;width:302px;height:278px;background:linear-gradient(135deg,#6b3a2a,#8a7a68 55%,#c8bfb2)" role="img" aria-label="Hotel lounge with brick wall, pendant lamps and grey armchairs"></div>
  <div class="photo" style="left:419px;top:516px;width:362px;height:603px;background:linear-gradient(180deg,#e9e6e1 0%,#b98a4e 35%,#8c5a30 55%,#d8d2c8 80%,#ece8e2)" role="img" aria-label="Marble hotel lobby with wooden columns and a crystal chandelier"></div>
  <div class="photo" style="left:830px;top:578px;width:286px;height:163px;background:linear-gradient(180deg,#8c8fd0 0%,#6a7fb8 40%,#3d7a6a 65%,#4a62b0 100%)" role="img" aria-label="Overwater villas on a calm lagoon at dusk"></div>
  <div class="photo" style="left:830px;top:789px;width:370px;height:265px;background:linear-gradient(135deg,#e6e6e6,#9a9a9a 45%,#2a2c33 75%,#1a1b20)" role="img" aria-label="Business class cabin with private leather seats"></div>
  <div class="photo" style="left:0;top:888px;width:368px;height:184px;background:linear-gradient(180deg,#4d6fa8 0%,#2c4a3a 40%,#d08a3a 65%,#2a7cc8 100%)" role="img" aria-label="Tropical resort with palm trees and lit pool at evening"></div>
</section>

<section class="partners">
  <p class="abs eyebrow-sans" style="left:225px;top:1337px">WE WORK DIRECTLY WITH</p>
  <div class="abs rule" style="left:423px;top:1345px;width:223px"></div>
  <h2 class="abs display" style="left:225px;top:1362px;font-size:49px;line-height:48px">Hotels and<br>Airlines to Get<br>You the Best<br>Price, always.</h2>
  <a class="abs btn" style="left:225px;top:1590px;width:153px;height:41px"><span class="frame"></span><span class="face">ADD SCREENSHOT</span></a>
  <div class="photo" style="left:410px;top:1707px;width:362px;height:287px;background:linear-gradient(180deg,#5d86b0 0%,#a9b4bb 50%,#e2b47a 62%,#3a3128 80%,#2a241d)" role="img" aria-label="Private jet on a runway at sunset"></div>
  <div class="photo" style="left:646px;top:1286px;width:370px;height:558px;background:linear-gradient(180deg,#8a6a40 0%,#c6a878 30%,#6b5a48 60%,#b39a78 100%)" role="img" aria-label="Traveller with a rolling suitcase opening a door in a hotel corridor"></div>
</section>

<section class="plans">
  <p class="abs eyebrow" style="left:0;top:2153px;width:1200px;text-align:center">TELL US ABOUT</p>
  <h2 class="abs display" style="left:0;top:2183px;width:1200px;text-align:center;font-size:55px">Your Next Holiday Plans.</h2>
  <p class="abs lede" style="left:0;top:2252px;width:1200px;text-align:center">The more details the better.</p>
  <div class="abs field"><span>Enter Your Keywords here</span></div>
  <a class="abs btn" style="left:540px;top:2482px;width:117px;height:41px"><span class="frame"></span><span class="face">SEND NOW</span></a>
</section>

<footer>
  <p class="abs copy">©2022 <b>Silken Roam</b>. All Rightes Reserved.</p>
  <div class="abs social" style="left:846px;top:2719px"></div>
  <div class="abs social" style="left:891px;top:2719px"></div>
  <div class="abs social" style="left:936px;top:2719px"></div>
</footer>
</body>
</html>
```